Law firm needs business card and letter head designed

I need a business card and a letter head for a law firm, well its not really a law firm as it is just me.
The letter head is to have the logo located on the top right hand side, with a footer designed as well. The footer will also be on the second page but the main logo design will not be on the second page.

The business card is to be doubled sided.

The business name is Bramwell Legal.

Industry/Entity Type

Legal

Requirements
Must have
• The letterhead is to have the logo top right hand side of the front page with email address tcorrigan@bramwelllegal.com.au and phone number 0432 817 265, with a footer designed that incorporates the logo, the footer is also to include the following wording Liability Limited by a scheme approved under Professional Standards Legislation.
• I would like the letterhead design to have a second page, with this page just having the footer design, the second page does not need to have the wording above.
• The business card is to be double sides, with one side having my name Tobias Corrigan and title Principal, along with the number 0432 817 265 and the email tcorrigan@bramwelllegal.com.au
• I would like a classy design but with some edge.

```html
<!DOCTYPE html>
<html lang="en">
<head>
<meta charset="utf-8">
<title>Bramwell Legal — Letterhead</title>
<link rel="stylesheet" href="https://fonts.googleapis.com/css2?family=Open+Sans:wght@400;600&display=swap">
<style>
  :root {
    --backdrop: #eeeff0;
    --paper: #fbfbfb;
    --ink: #3d4148;
    --teal: #2a7a97;
    --rule: #d9dcdf;
    --on-teal: #ffffff;
  }
  * { box-sizing: border-box; margin: 0; padding: 0; }
  html, body {
    width: 1200px; height: 795px; overflow: hidden;
    background: var(--backdrop);
    font-family: "Open Sans", Arial, sans-serif;
    color: var(--ink);
  }
  .letterhead {
    position: absolute; left: 340px; top: 30px;
    width: 520px; height: 736px;
    background: var(--paper);
    box-shadow: 0 2px 10px rgba(0,0,0,0.08);
    overflow: hidden;
  }
  .brand {
    position: absolute; right: 52px; top: 50px;
    display: flex; align-items: center; gap: 7px;
  }
  .brand-square { width: 12px; height: 12px; background: var(--teal); flex-shrink: 0; }
  .brand-name {
    font-size: 12px; font-weight: 600; letter-spacing: 1.5px;
    color: var(--teal); text-transform: uppercase; white-space: nowrap;
  }
  .letter {
    position: absolute; left: 52px; top: 150px; width: 400px;
    font-size: 7.6px; line-height: 1.45;
  }
  .salutation { font-size: 11px; margin-bottom: 14px; }
  .letter p { margin-bottom: 11px; }
  .sign-off { margin-top: 18px; }
  .signatory { margin-top: 30px; margin-left: 30px; }
  .signatory-name { font-size: 8.5px; color: var(--teal); letter-spacing: 0.5px; }
  .signatory-title { font-size: 6.5px; color: var(--ink); }
  .footer { position: absolute; left: 0; bottom: 0; width: 520px; height: 140px; }
  .footer-wave { position: absolute; left: 0; top: 0; }
  .footer-contact {
    position: absolute; right: 24px; bottom: 34px;
    display: flex; gap: 12px;
    font-size: 7.5px; line-height: 1; color: var(--on-teal);
    white-space: nowrap;
  }
  .contact-item { display: inline-flex; align-items: center; gap: 4px; }
  .contact-icon { flex-shrink: 0; display: block; }
  .footer-legal {
    position: absolute; right: 24px; bottom: 18px;
    font-size: 6.5px; color: var(--on-teal); white-space: nowrap;
  }
</style>
</head>
<body>
  <main class="letterhead">
    <header class="brand">
      <span class="brand-square"></span>
      <span class="brand-name">Bramwell Legal</span>
    </header>

    <section class="letter">
      <div class="salutation">Dear Mr. Reeve,</div>
      <p>Lorem ipsum dolor sit amet, consectetur adipiscing elit. Donec orci purus, luctus vitae dignissim eu, iaculis sed purus. Vivamus faucibus, ipsum nec aliquet viverra, leo mauris condimentum ligula, sit amet sagittis enim ligula quis arcu. Nam egestas tortor id nisi porttitor mattis. In tortor ante, ultricies in suscipit a, tempus non massa. Vivamus et auctor mi. Fusce vel massa nulla. Phasellus nec eros mauris, et scelerisque orci.</p>
      <p>Donec malesuada orci vitae nulla accumsan porta a id massa. Quisque accumsan iaculis magna sit amet fringilla. Maecenas consequat, magna eget tincidunt semper, odio nibh rutrum mi, id feugiat ante nisi eu risus. Vestibulum nunc orci, rhoncus a placerat in, ultricies in mi. Cras mattis varius eros, vel fringilla nisi suscipit eget. Quisque scelerisque sagittis nulla at porttitor.</p>
      <p>Sed id augue vitae urna euismod commodo aliquet a quam. Pellentesque arcu velit, cursus et malesuada ut, consequat et diam. Nullam erat sem, rhoncus id ullamcorper vitae, rhoncus et arcu. In ultricies ultricies nulla, ut rutrum nisi iaculis at. Donec eu magna a metus ornare faucibus. Fusce aliquet faucibus ultricies. Morbi semper, est id tincidunt gravida, sem arcu adipiscing lacus, ac bibendum nulla leo eu purus. Quisque nec diam sed risus consectetur accumsan quis quis nibh. Vestibulum id purus lorem.</p>
      <p>It is a long established fact that a reader will be distracted by the readable content of a page when looking at its layout. The point of using Lorem Ipsum is that it has a more-or-less normal distribution of letters, as opposed to using 'Content here, content here', making it look like readable English. Many desktop publishing packages</p>
      <div class="sign-off">Sincerely,</div>
      <div class="signatory">
        <div class="signatory-name">DANIEL REEVE</div>
        <div class="signatory-title">CEO/Founder</div>
      </div>
    </section>

    <footer class="footer">
      <svg class="footer-wave" width="520" height="140" viewBox="0 0 520 140" aria-hidden="true">
        <path d="M0 134 Q 250 108 520 14" fill="none" stroke="var(--rule)" stroke-width="1.5"/>
        <path d="M0 122 Q 260 84 520 28 L520 140 L0 140 Z" fill="var(--teal)"/>
      </svg>
      <div class="footer-contact">
        <span class="contact-item">
          <svg class="contact-icon" width="7" height="7" viewBox="0 0 10 10" aria-hidden="true"><path d="M2 1 L4 1 L5 3.5 L3.8 4.5 Q5 6.5 6.5 6.2 L7.5 5 L9.5 6 L9.5 8 Q9 9.5 7 9 Q1 7 1 2 Z" fill="currentColor"/></svg>
          <span>0432 817 265</span>
        </span>
        <span class="contact-item">
          <svg class="contact-icon" width="8" height="6" viewBox="0 0 10 7" aria-hidden="true"><rect x="0.5" y="0.5" width="9" height="6" fill="none" stroke="currentColor"/><path d="M0.5 0.5 L5 4 L9.5 0.5" fill="none" stroke="currentColor"/></svg>
          <span>tcorrigan@bramwelllegal.com.au</span>
        </span>
        <span class="contact-item">
          <svg class="contact-icon" width="7" height="7" viewBox="0 0 10 10" aria-hidden="true"><circle cx="5" cy="5" r="4.3" fill="none" stroke="currentColor"/><path d="M0.7 5 H9.3 M5 0.7 Q2 5 5 9.3 Q8 5 5 0.7" fill="none" stroke="currentColor" stroke-width="0.8"/></svg>
          <span>www.bramwelllegal.com.au</span>
        </span>
      </div>
      <div class="footer-legal">Liability Limited by a scheme approved under Professional Standards Legislation.</div>
    </footer>
  </main>
</body>
</html>
```